Brookvale Strategy Partners Website Design

I need a website design for my new business consulting and executive coaching firm, Brookvale Strategy Partners. We provide consultative services to business C-suites as well as personal coaching to executives. I have attached the logo with color scheme I have chosen. I would like the website to reflect professionalism and continue the color scheme in the logo.

Target Market(s)

Small to medium business and their executives; middle to upper income men and women in mid- to late career looking for significance

Industry/Entity Type

Business Consultant

Number of Pages Required

4 page

Requirements
Must have
• A homepage with prominent logo and way to contact for more information; an area on the homepage with easy to read, clear text to describe what the company does; a prominent area on the homepage for a tagline; a blog page that can be updated regularly, an "about us" page with biographical information; an "about us" page; a page detailing services offered
• The web design must match the logo colors and font that I have uploaded.
Nice to have
• A lighthouse picture in the background or header
Should not have
• A lot of text area on the homepage

```html
<!DOCTYPE html>
<html lang="en">
<head>
<meta charset="utf-8">
<title>Brookvale Strategy Partners</title>
<link href="https://fonts.googleapis.com/css2?family=Lato:wght@400;700&family=Noto+Serif:wght@400&display=swap" rel="stylesheet">
<style>
:root{
  --red:#6e0e10;
  --navy:#1c2b5a;
  --ink:#555;
  --page:#fafafa;
  --footer:#efefef;
  --white:#fff;
  --rule:#d8d8d8;
}
*{margin:0;padding:0;box-sizing:border-box}
html,body{width:1170px;height:1200px;overflow:hidden}
body{position:relative;background:var(--page);font-family:'Lato',sans-serif;color:var(--ink)}
.serif{font-family:'Noto Serif',serif}
.abs{position:absolute}

.site-header{position:absolute;left:0;top:0;width:1170px;height:142px;background:var(--white)}
.brand{left:158px;top:34px;display:flex;align-items:center;gap:10px}
.brand-mark{width:26px;height:26px;background:var(--navy)}
.brand-name{font-family:'Noto Serif',serif;font-size:15px;line-height:19px;color:var(--navy);text-transform:uppercase;letter-spacing:.5px;width:140px}
.enquiry{left:655px;top:36px;display:flex;align-items:center;gap:9px;font-weight:700;font-size:15px;color:var(--navy)}
.social{left:910px;top:35px;display:flex;gap:5px}
.social span{width:22px;height:22px;border-radius:50%;background:var(--navy);display:block}
.band{left:0;top:118px;width:1170px;height:24px;background:var(--red)}
.nav-bar{left:315px;top:97px;width:855px;height:45px;background:var(--red);clip-path:polygon(20px 0,100% 0,100% 100%,0 100%)}
.main-nav{left:0;top:97px;width:1170px;height:45px}
.main-nav a{position:absolute;top:13px;transform:translateX(-50%);font-family:'Noto Serif',serif;font-size:13.5px;color:var(--white);text-decoration:none;white-space:nowrap}
.nav-shade{left:0;top:141px;width:1170px;height:1px;background:#c9c9c9}

.hero-photo{left:0;top:142px;width:1170px;height:366px;
  background:radial-gradient(ellipse at 80% 30%,rgba(205,170,170,.55),transparent 45%),
  radial-gradient(ellipse at 20% 55%,rgba(180,150,165,.45),transparent 40%),
  linear-gradient(180deg,#6d6f88 0%,#4a5478 55%,#1f3566 100%)}
.hero-title{left:158px;top:190px;font-family:'Noto Serif',serif;font-size:28px;line-height:35px;color:var(--white);width:520px}
.hero-text{left:158px;top:284px;font-size:14.5px;line-height:24px;color:var(--white);width:520px}
.hero-link{left:158px;top:386px;font-weight:700;font-size:14px;color:var(--white);display:flex;align-items:center;gap:8px}

.service-card{position:absolute;top:484px;width:193px;height:107px;background:var(--white);box-shadow:0 1px 3px rgba(0,0,0,.18);text-align:center}
.service-card svg{position:absolute;left:50%;top:14px;transform:translateX(-50%)}
.service-card hr{position:absolute;left:15px;right:15px;top:68px;border:0;border-top:1px solid var(--rule)}
.service-card h3{position:absolute;left:0;right:0;top:78px;font-family:'Noto Serif',serif;font-weight:400;font-size:13.5px;color:#444;letter-spacing:.3px}

.about{left:158px;top:634px;width:582px}
.about h2{font-family:'Noto Serif',serif;font-weight:400;font-size:19px;color:var(--red);padding-bottom:12px;border-bottom:1px solid var(--rule)}
.about p{font-size:11.5px;line-height:19px;margin-top:16px}
.about p:first-of-type{margin-top:14px}
.read-more{display:block;margin-top:18px;font-size:12px;color:var(--red)}

.news{left:778px;top:634px;width:235px;height:242px;background:var(--white);box-shadow:0 1px 3px rgba(0,0,0,.18)}
.news h2{background:var(--red);height:38px;padding:7px 15px;font-family:'Noto Serif',serif;font-weight:400;font-size:17px;color:var(--white)}
.news-item{padding:0 15px;margin-top:16px}
.news-item time{display:block;font-size:12px;color:var(--navy)}
.news-item p{font-size:11.5px;line-height:19px;margin-top:1px}

.site-footer{left:0;top:925px;width:1170px;height:231px;background:var(--footer)}
.footer-col{position:absolute;top:956px}
.footer-col h4{font-family:'Noto Serif',serif;font-weight:400;font-size:15px;color:var(--navy);margin-bottom:16px}
.footer-col li{list-style:none;font-size:12px;line-height:26.3px}
.footer-brand{left:790px;top:1005px;width:200px;display:flex;align-items:center;gap:12px}
.footer-brand .brand-mark{width:34px;height:34px}
.footer-brand span{font-family:'Noto Serif',serif;font-size:18px;line-height:23px;color:var(--navy);text-transform:uppercase}
.copyright{left:0;top:1156px;width:1170px;height:44px;background:var(--navy);color:var(--white);font-family:'Noto Serif',serif;font-size:12px;text-align:center;line-height:44px}
</style>
</head>
<body>

<header class="site-header">
  <div class="abs brand"><span class="brand-mark"></span><span class="brand-name">Brookvale Strategy Partners</span></div>
  <div class="abs enquiry">
    <svg width="18" height="20" viewBox="0 0 18 20"><rect x="1" y="3" width="5" height="16" rx="1" fill="#6e0e10"/><rect x="7" y="1" width="10" height="18" rx="1" fill="#6e0e10"/><g fill="#fff"><rect x="9" y="4" width="6" height="3"/><rect x="9" y="9" width="2" height="2"/><rect x="12.5" y="9" width="2" height="2"/><rect x="9" y="13" width="2" height="2"/><rect x="12.5" y="13" width="2" height="2"/></g></svg>
    For enquiries, call 555 014 2290
  </div>
  <div class="abs social"><span></span><span></span><span></span><span></span></div>
</header>
<div class="abs band"></div>
<div class="abs nav-bar"></div>
<nav class="abs main-nav">
  <a style="left:384px">HOME</a>
  <a style="left:512px">ABOUT US</a>
  <a style="left:667px">OUR SERVICES</a>
  <a style="left:807px">BLOG</a>
  <a style="left:941px">CONTACT US</a>
</nav>
<div class="abs nav-shade"></div>

<section>
  <div class="abs hero-photo" role="img" aria-label="Lighthouse on a rocky outcrop beneath a cloudy dusk sky"></div>
  <h1 class="abs hero-title" style="font-weight:400">Trusted Advisor in Business Consulting and Coaching.</h1>
  <p class="abs hero-text">Typi non habent claritatem insitam legentis in iis qui facit eorum claritatem. Investigationes demonstraverunt lectores legere me lius quod legunt saepius, claritas est etiam processus dynamicus.</p>
  <div class="abs hero-link">LEARN MORE
    <svg width="14" height="12" viewBox="0 0 14 12"><path d="M1 6h11M7 1l5 5-5 5" stroke="#fff" stroke-width="2" fill="none"/></svg>
  </div>
</section>

<section>
  <div class="service-card" style="left:158px">
    <svg width="40" height="40" viewBox="0 0 40 40"><g fill="#1c2b5a"><circle cx="20" cy="20" r="14"/><g><rect x="17" y="1" width="6" height="8"/><rect x="17" y="31" width="6" height="8"/><rect x="1" y="17" width="8" height="6"/><rect x="31" y="17" width="8" height="6"/><rect x="17" y="1" width="6" height="8" transform="rotate(45 20 20)"/><rect x="17" y="1" width="6" height="8" transform="rotate(135 20 20)"/><rect x="17" y="1" width="6" height="8" transform="rotate(225 20 20)"/><rect x="17" y="1" width="6" height="8" transform="rotate(315 20 20)"/></g></g><circle cx="20" cy="20" r="10" fill="#fff"/><circle cx="20" cy="16" r="3.5" fill="#1c2b5a"/><path d="M13 27c1-5 13-5 14 0z" fill="#1c2b5a"/></svg>
    <hr><h3>BUSINESS CONSULTING</h3>
  </div>
  <div class="service-card" style="left:379px">
    <svg width="40" height="40" viewBox="0 0 40 40"><path d="M14 10V6h12v4" stroke="#1c2b5a" stroke-width="3" fill="none"/><rect x="4" y="10" width="32" height="24" rx="3" fill="#1c2b5a"/><path d="M4 21h32" stroke="#fff" stroke-width="1.5"/><rect x="16" y="18" width="8" height="6" fill="#fff"/><rect x="18" y="20" width="4" height="2" fill="#1c2b5a"/></svg>
    <hr><h3>CAREER ADVISORY</h3>
  </div>
  <div class="service-card" style="left:600px">
    <svg width="56" height="40" viewBox="0 0 56 40"><g fill="#1c2b5a"><circle cx="12" cy="13" r="6"/><path d="M1 36c0-12 22-12 22 0z"/><circle cx="44" cy="13" r="6"/><path d="M33 36c0-12 22-12 22 0z"/><circle cx="28" cy="10" r="7" stroke="#fff" stroke-width="1.5"/><path d="M14 38c0-15 28-15 28 0z" stroke="#fff" stroke-width="1.5"/></g></svg>
    <hr><h3>PERSONAL COACHING</h3>
  </div>
  <div class="service-card" style="left:820px">
    <svg width="48" height="40" viewBox="0 0 48 40"><g fill="#1c2b5a"><rect x="0" y="8" width="10" height="14" transform="rotate(-40 5 15)"/><rect x="38" y="8" width="10" height="14" transform="rotate(40 43 15)"/><path d="M10 18l12-10 8 4 9 2-10 20-6 2-13-9z"/></g><path d="M20 16l6 4M18 22l8 6M15 26l6 5" stroke="#fff" stroke-width="1.5"/></svg>
    <hr><h3>OUTSOURCING</h3>
  </div>
</section>

<section class="abs about">
  <h2>About Brookvale Strategy Partners</h2>
  <p>Lorem ipsum dolor sit amet, consectetuer adipiscing elit, sed diam nonummy nibh euismod tincidunt ut laoreet dolore magna aliquam erat volutpat. Ut wisi enim ad minim veniam, quis nostrud exerci tation ullamcorper suscipit lobortis nisl ut aliquip ex ea commodo consequat.</p>
  <p>Duis autem vel eum iriure dolor in hendrerit in vulputate velit esse molestie consequat, vel illum dolore eu feugiat nulla facilisis at vero eros et accumsan et iusto odio dignissim qui blandit praesent luptatum zzril delenit augue duis dolore te feugait nulla facilisi.</p>
  <a class="read-more">READ MORE &nbsp;&raquo;</a>
</section>

<aside class="abs news">
  <h2>In The News</h2>
  <div class="news-item"><time>30 December 2015</time><p>Claritas est etiam processus dynamicus, qui sequitur mutationem consecteuer lectorum nam et libero parum.</p></div>
  <div class="news-item"><time>29 December 2015</time><p>Ut wisi enim ad minim veniam, quis nostrud exerci tation ullamcorper suscipit lobortis.</p></div>
</aside>

<footer>
  <div class="abs site-footer"></div>
  <div class="footer-col" style="left:158px"><h4>Quick Links</h4><ul><li>Home</li><li>About Us</li><li>Services</li><li>Blog</li><li>Contact Us</li></ul></div>
  <div class="footer-col" style="left:333px"><h4>Our Services</h4><ul><li>Business Consulting</li><li>Career Advisory</li><li>Personal Coaching</li><li>Outsourcing</li></ul></div>
  <div class="footer-col" style="left:543px"><h4>Contact Our Office</h4><ul><li>Brookvale Strategy Partners</li><li>48 Harbor Lane</li><li>Brookvale, OH 44010</li><li>info@brookvale-strategy.com</li></ul></div>
  <div class="abs footer-brand"><span class="brand-mark"></span><span>Brookvale Strategy Partners</span></div>
  <div class="abs copyright">© 2015 Brookvale Strategy Partners. All rights reserved.</div>
</footer>

</body>
</html>
```